Invitation Design Project

50th Birthday Party for Tim. Big, loud party planned with loads of friends and family. at our home. Decorations will be coloured lanterns attached to the pergola and hired a band.

Details:

on 19th October, 2013
(other details when design chosen)
at: 7.00 pm
RSVP: 14th October, 2013

```html
<!DOCTYPE html>
<html lang="en">
<head>
<meta charset="utf-8">
<title>Tim's 50th Birthday Invitation</title>
<link rel="stylesheet" href="https://fonts.googleapis.com/css2?family=Cormorant+Garamond:ital,wght@0,500;1,500;1,600&display=swap">
<style>
  :root {
    --paper: #f7f4e6;
    --ink: #7a785f;
    --accent: #19b6b8;
    --vine: #6f6d55;
    --bloom-yellow: #f2c21a;
    --bloom-green: #8fb04a;
  }
  html, body {
    margin: 0;
    padding: 0;
    overflow: hidden;
    background: var(--paper);
  }
  .invitation {
    position: relative;
    width: 849px;
    height: 1200px;
    background: var(--paper);
    overflow: hidden;
    font-family: "Cormorant Garamond", Georgia, serif;
    color: var(--ink);
  }
  .floral-vine {
    position: absolute;
    left: 150px;
    top: 12px;
    width: 690px;
    height: 430px;
    border-radius: 48% 52% 40% 60% / 55% 60% 40% 45%;
    background:
      radial-gradient(ellipse at 25% 45%, rgba(242,194,26,0.35), transparent 55%),
      radial-gradient(ellipse at 70% 40%, rgba(25,182,184,0.30), transparent 55%),
      radial-gradient(ellipse at 50% 30%, rgba(111,109,85,0.30), transparent 65%);
  }
  .line {
    position: absolute;
    left: 0;
    width: 100%;
    margin: 0;
    text-align: center;
    line-height: 1;
    white-space: nowrap;
  }
  .line--italic { font-style: italic; font-weight: 500; font-size: 39px; }
  .line--roman { font-style: normal; font-weight: 500; font-size: 41px; }
  .greeting { top: 455px; }
  .welcome { top: 501px; }
  .honour { top: 551px; }
  .guest-name {
    top: 595px;
    font-style: italic;
    font-weight: 600;
    font-size: 118px;
    color: var(--accent);
  }
  .age-line { top: 733px; }
  .age-number { color: var(--accent); font-size: 50px; font-weight: 600; }
  .date { top: 813px; }
  .time { top: 859px; }
  .address-street { top: 934px; }
  .address-town { top: 983px; }
  .rsvp { top: 1063px; }
  .phone { top: 1114px; }
</style>
</head>
<body>
  <main class="invitation">
    <div class="floral-vine" role="img" aria-label="Swirling olive vine ornament with small yellow, teal and green flowers and leaves"></div>

    <p class="line line--italic greeting">Its a great Celebration !!</p>
    <p class="line line--italic welcome">Please join us for food and fun</p>
    <p class="line line--italic honour">in honour of</p>
    <h1 class="line guest-name">Tim</h1>
    <p class="line line--italic age-line">who is turning <span class="age-number">50</span>!</p>

    <p class="line line--roman date">On 19th October, 2013</p>
    <p class="line line--roman time">at 7:00 p.m.</p>

    <p class="line line--italic address-street">0000 Any Street west</p>
    <p class="line line--italic address-town">Townsvlle , ST&nbsp; 0000</p>

    <p class="line line--italic rsvp">RSVP by 14th October, 2013</p>
    <p class="line line--italic phone">phone 000 000 000</p>
  </main>
</body>
</html>
```